Letterhead Design Project

Standard A4 paper, center the name Brightway Wash (with the mop) same as front of business card.
47 Harbour Vale Rd Kelston 5062 ABN: 71205839416
M. 0427163958 T. 83917605 Calibri font

Industry/Entity Type

Business

```html
<!DOCTYPE html>
<html lang="en">
<head>
<meta charset="utf-8">
<title>Brightway Wash Letterhead</title>
<link href="https://fonts.googleapis.com/css2?family=Carlito:wght@400;700&display=swap" rel="stylesheet">
<style>
  :root {
    --backdrop: #e6e6e6;
    --paper: #f4f4f4;
    --brand-blue: #1c8fd2;
    --deep-blue: #1e9bd7;
    --pale-blue: #d3e8f0;
    --text-grey: #8a8a8a;
  }
  html, body {
    margin: 0;
    padding: 0;
    width: 1200px;
    height: 968px;
    overflow: hidden;
    background: var(--backdrop);
    font-family: "Carlito", "Calibri", sans-serif;
  }
  .letterhead {
    position: absolute;
    left: 282px;
    top: 34px;
    width: 636px;
    height: 900px;
    background: var(--paper);
    overflow: hidden;
    box-shadow: 0 2px 10px rgba(0,0,0,0.12);
  }
  .letterhead__top,
  .letterhead__bottom {
    position: absolute;
    left: 0;
    width: 636px;
    height: 210px;
    display: block;
  }
  .letterhead__top { top: 0; }
  .letterhead__bottom { bottom: 0; transform: rotate(180deg); }
  .masthead {
    position: absolute;
    top: 138px;
    left: 0;
    width: 636px;
    text-align: center;
  }
  .masthead__name {
    display: inline-flex;
    align-items: center;
    gap: 10px;
    margin: 0;
    font-size: 31px;
    font-weight: 400;
    letter-spacing: 0.5px;
    text-transform: uppercase;
    color: var(--brand-blue);
    line-height: 1;
  }
  .masthead__mark {
    width: 22px;
    height: 22px;
    border-radius: 50%;
    background: var(--brand-blue);
    flex: none;
  }
  .masthead__address,
  .masthead__abn,
  .masthead__contact {
    margin: 2px 0 0;
    font-size: 11px;
    color: var(--text-grey);
    line-height: 1.2;
  }
  .masthead__address { margin-top: 7px; }
  .masthead__label { color: var(--brand-blue); }
</style>
</head>
<body>
  <main class="letterhead">
    <svg class="letterhead__top" viewBox="0 0 636 210" aria-hidden="true">
      <defs>
        <linearGradient id="bandFade" x1="0" y1="0" x2="1" y2="0">
          <stop offset="0" stop-color="var(--deep-blue)"/>
          <stop offset="0.45" stop-color="#9fd0e8"/>
          <stop offset="1" stop-color="var(--pale-blue)"/>
        </linearGradient>
        <linearGradient id="splashFade" x1="0" y1="0" x2="1" y2="0">
          <stop offset="0" stop-color="#1a8fcf"/>
          <stop offset="0.6" stop-color="#6cc0e8"/>
          <stop offset="1" stop-color="#cfeaf6" stop-opacity="0"/>
        </linearGradient>
      </defs>
      <path class="corner-band" d="M0 0 H636 V205 C520 130 330 75 0 58 Z" fill="url(#bandFade)"/>
      <path role="img" aria-label="Flowing water splash with droplets" d="M0 50 C80 46 150 58 200 74 C240 86 280 100 320 118 C270 106 230 96 190 88 C130 74 70 66 0 66 Z" fill="url(#splashFade)"/>
    </svg>

    <header class="masthead">
      <h1 class="masthead__name"><span class="masthead__mark" aria-hidden="true"></span>Brightway Wash</h1>
      <p class="masthead__address">47 Harbour Vale Rd, Kelston 5062</p>
      <p class="masthead__abn"><span class="masthead__label">ABN:</span> 71205839416</p>
      <p class="masthead__contact"><span class="masthead__label">M.</span> 0427163958 &nbsp;<span class="masthead__label">T.</span> 83917605</p>
    </header>

    <svg class="letterhead__bottom" viewBox="0 0 636 210" aria-hidden="true">
      <defs>
        <linearGradient id="bandFadeLow" x1="0" y1="0" x2="1" y2="0">
          <stop offset="0" stop-color="var(--deep-blue)"/>
          <stop offset="0.45" stop-color="#9fd0e8"/>
          <stop offset="1" stop-color="var(--pale-blue)"/>
        </linearGradient>
        <linearGradient id="splashFadeLow" x1="0" y1="0" x2="1" y2="0">
          <stop offset="0" stop-color="#1a8fcf"/>
          <stop offset="0.6" stop-color="#6cc0e8"/>
          <stop offset="1" stop-color="#cfeaf6" stop-opacity="0"/>
        </linearGradient>
      </defs>
      <path class="corner-band" d="M0 0 H636 V205 C520 130 330 75 0 58 Z" fill="url(#bandFadeLow)"/>
      <path role="img" aria-label="Flowing water splash with droplets" d="M0 50 C80 46 150 58 200 74 C240 86 280 100 320 118 C270 106 230 96 190 88 C130 74 70 66 0 66 Z" fill="url(#splashFadeLow)"/>
    </svg>
  </main>
</body>
</html>
```